Oven Cleaning Business owner needs business card design

Hi there,
Would like for a business card to be designed for myself, the owner of a professional oven cleaning business on the Sunshine Coast.
Would like it to look sleek, and modern-ish. Bit creative is encouraged too.
Include following:
Name/title: Corin ter Haghe, Owner
Phone number: 1300 482 916
Email: info@hearthshinecrew.com.au
Website: www.hearthshinecrew.com.au

```html
<!DOCTYPE html>
<html lang="en">
<head>
<meta charset="utf-8">
<title>Hearthshine Crew – Business Card</title>
<link rel="stylesheet" href="https://fonts.googleapis.com/css2?family=Montserrat:wght@400;500;800&family=Lexend:wght@300&display=swap">
<style>
  :root {
    --stage: #141414;
    --teal: #53c3ca;
    --ink: #0d0d0d;
    --text: #3a3a3a;
    --paper: #ffffff;
  }
  * { margin: 0; padding: 0; box-sizing: border-box; }
  html, body { width: 1200px; height: 848px; overflow: hidden; background: var(--stage); }
  .canvas { position: relative; width: 1200px; height: 848px; font-family: "Montserrat", sans-serif; }

  .card { position: absolute; left: 281px; width: 615px; height: 334px; }
  .card--front { top: 68px; background: var(--teal); }
  .card--back { top: 445px; background: var(--paper); }

  .front-brand {
    position: absolute; left: 0; right: 0; top: 112px;
    text-align: center; color: var(--ink); font-weight: 800;
  }
  .front-brand__main { display: block; font-size: 46px; letter-spacing: 0.02em; line-height: 1; }
  .front-brand__sub { display: block; font-size: 20px; letter-spacing: 0.62em; margin-top: 16px; padding-left: 0.62em; line-height: 1; }

  .back-brand { position: absolute; left: 61px; top: 139px; display: flex; align-items: center; gap: 14px; }
  .back-brand__dot { width: 54px; height: 54px; border-radius: 50%; background: var(--teal); }
  .back-brand__name { color: var(--ink); font-weight: 800; line-height: 1; }
  .back-brand__main { display: block; font-size: 15px; letter-spacing: 0.03em; }
  .back-brand__sub { display: block; font-size: 9px; letter-spacing: 0.6em; margin-top: 6px; }

  .divider { position: absolute; left: 307px; top: 113px; width: 1px; height: 108px; background: var(--teal); }

  .contact { position: absolute; left: 333px; top: 106px; }
  .contact__name { font-family: "Lexend", sans-serif; font-weight: 300; font-size: 24px; color: var(--teal); line-height: 1.1; }
  .contact__role { font-size: 13px; color: var(--text); margin-top: 2px; }
  .contact__list { list-style: none; margin-top: 18px; }
  .contact__item { display: flex; align-items: center; gap: 8px; font-size: 13px; color: var(--text); height: 19px; }
  .contact__icon { width: 12px; height: 12px; flex: none; }
</style>
</head>
<body>
<div class="canvas">

  <section class="card card--front">
    <div class="front-brand">
      <span class="front-brand__main">HEARTHSHINE</span>
      <span class="front-brand__sub">CREW</span>
    </div>
  </section>

  <section class="card card--back">
    <div class="back-brand">
      <span class="back-brand__dot"></span>
      <span class="back-brand__name">
        <span class="back-brand__main">HEARTHSHINE</span>
        <span class="back-brand__sub">CREW</span>
      </span>
    </div>

    <div class="divider"></div>

    <div class="contact">
      <p class="contact__name">Corin ter Haghe</p>
      <p class="contact__role">Owner</p>
      <ul class="contact__list">
        <li class="contact__item">
          <svg class="contact__icon" viewBox="0 0 24 24" aria-hidden="true"><path fill="none" stroke="#53c3ca" stroke-width="2.2" stroke-linecap="round" stroke-linejoin="round" d="M5 3h4l2 5-2.5 1.5a11 11 0 0 0 6 6L16 13l5 2v4a2 2 0 0 1-2 2A16 16 0 0 1 3 5a2 2 0 0 1 2-2z"/></svg>
          1300 482 916
        </li>
        <li class="contact__item">
          <svg class="contact__icon" viewBox="0 0 24 24" aria-hidden="true"><rect x="2" y="5" width="20" height="14" fill="#53c3ca"/><path d="M2 5l10 8 10-8" fill="none" stroke="#fff" stroke-width="1.8"/></svg>
          info@hearthshinecrew.com.au
        </li>
        <li class="contact__item">
          <svg class="contact__icon" viewBox="0 0 24 24" aria-hidden="true"><g fill="none" stroke="#53c3ca" stroke-width="1.8"><circle cx="12" cy="12" r="9.5"/><ellipse cx="12" cy="12" rx="4" ry="9.5"/><path d="M2.5 12h19M4 7h16M4 17h16"/></g></svg>
          www.hearthshinecrew.com.au
        </li>
      </ul>
    </div>
  </section>

</div>
</body>
</html>
```